Vantrel Card

We want a business card that shows people who we are the log attached was designed by the designers on craft hive,we are using the OO in the logo (speech bubbles as our icon,so please make that part of the card ) keep the colouring the same as the logo design and we will be using high end production on the card using silver foil as the icon to make it stand out.
As Vantrel we specialise in finding influencers through social networks for brands, so if you used flimbo to comment about sports products and you were followed by of lot of users and interacted with those users then the algorithm finds you and we contact you to work for our clients as a company we then have a set of influencers that we use to support new sports products.
Also we use our algorithm to help athletes,models etc to be scored via there digital influence so when say Vorta KX ask me to find a skater that is not so much a podium rider but is more digital focused for a digital campaign then we work out who those guys or girls are to help Vorta KX
Vantrel is the name of the product and company, However I just wanted to give you the rationale of why we chose vantrel in the first place. Marbo itself is an 'abbreviation' from the proper name Alsander Wick from Tale of the Iron Hills. The character was able to look into the eskavor (sometimes translated as "Seeing Stone" but literally meaning "Farsighted" or "One that Sees from Afar") and see into the far corners of the Universe. Much in the same way as the platform has been developed is able to look into the far corners of the social network arena to help brands and Athletes will be able to see how they rated....but don't worry i don't go running around in the woods with a foam Axe and an army of dwarfs!!!
Digital Directors,Brand Directors,Athletes,Models,Celebrities and agents
Business

```html
<!DOCTYPE html>
<html lang="en">
<head>
<meta charset="utf-8">
<title>Vantrel Business Card</title>
<link rel="stylesheet" href="https://fonts.googleapis.com/css2?family=Open+Sans:wght@400;600;700&display=swap">
<style>
  :root {
    --page-bg: #e6e6e6;
    --card-white: #ffffff;
    --brand-blue: #52bdec;
    --stripe-grey: #858a8e;
    --ink-white: #ffffff;
  }
  html, body {
    margin: 0;
    padding: 0;
    width: 1200px;
    height: 960px;
    overflow: hidden;
    background: var(--page-bg);
    font-family: "Open Sans", Arial, sans-serif;
  }
  .canvas {
    position: relative;
    width: 1200px;
    height: 960px;
  }
  .card {
    position: absolute;
    left: 100px;
    top: 195px;
    width: 1000px;
    height: 570px;
    background: var(--card-white);
    box-shadow: 0 6px 24px rgba(0,0,0,0.18);
    overflow: hidden;
  }
  .brand-side {
    position: absolute;
    left: 0;
    top: 0;
    width: 540px;
    height: 100%;
    display: flex;
    align-items: center;
    justify-content: center;
  }
  .brand-name {
    font-family: "Open Sans", Arial, sans-serif;
    font-weight: 700;
    font-size: 104px;
    letter-spacing: -2px;
    color: var(--brand-blue);
    line-height: 1;
    margin-top: 60px;
  }
  .stripe {
    position: absolute;
    top: 0;
    width: 12px;
    height: 100%;
    background: var(--stripe-grey);
  }
  .stripe--left { left: 540px; }
  .stripe--right { left: 904px; }
  .info-panel {
    position: absolute;
    left: 564px;
    top: 0;
    width: 328px;
    height: 100%;
    background: var(--brand-blue);
    color: var(--ink-white);
  }
  .person {
    position: absolute;
    left: 38px;
    top: 70px;
  }
  .person-name {
    font-weight: 700;
    font-size: 27px;
    margin: 0;
    line-height: 1.2;
  }
  .person-role {
    font-weight: 400;
    font-size: 23px;
    margin: 0;
    line-height: 1.2;
  }
  .contact-list {
    position: absolute;
    left: 30px;
    top: 310px;
    list-style: none;
    margin: 0;
    padding: 0;
    font-size: 17px;
    line-height: 1.3;
  }
  .contact-item {
    display: flex;
    align-items: flex-start;
    margin-bottom: 7px;
  }
  .contact-icon {
    flex: none;
    width: 18px;
    height: 18px;
    margin-right: 9px;
    margin-top: 2px;
  }
  .address-lines { display: block; }
  .end-strip {
    position: absolute;
    left: 916px;
    top: 0;
    width: 84px;
    height: 100%;
    background: var(--card-white);
  }
</style>
</head>
<body>
<div class="canvas">
  <div class="card">
    <div class="brand-side">
      <span class="brand-name">vantrel</span>
    </div>

    <div class="stripe stripe--left"></div>

    <div class="info-panel">
      <div class="person">
        <p class="person-name">Dorin Halloway</p>
        <p class="person-role">Owner / C.E.O</p>
      </div>

      <ul class="contact-list">
        <li class="contact-item">
          <svg class="contact-icon" viewBox="0 0 18 18"><circle cx="9" cy="9" r="9" fill="#fff"/><path d="M9 3.5a3.2 3.2 0 0 0-3.2 3.2c0 2.4 3.2 6.3 3.2 6.3s3.2-3.9 3.2-6.3A3.2 3.2 0 0 0 9 3.5z" fill="#52bdec"/><circle cx="9" cy="6.7" r="1.2" fill="#fff"/></svg>
          <span class="address-lines">Suite # 418, Kelm Bldg,<br>NY 82471</span>
        </li>
        <li class="contact-item">
          <svg class="contact-icon" viewBox="0 0 18 18"><circle cx="9" cy="9" r="9" fill="#fff"/><path d="M6 4.5l1.8 0 .8 2.4-1.2 1c.6 1.3 1.5 2.2 2.7 2.8l1-1.2 2.4.8v1.8c0 .6-.5 1-1.1 1C8.5 13 5 9.5 5 5.6c0-.6.4-1.1 1-1.1z" fill="#52bdec"/></svg>
          <span>555-214-7731</span>
        </li>
        <li class="contact-item">
          <svg class="contact-icon" viewBox="0 0 18 18"><circle cx="9" cy="9" r="9" fill="#fff"/><rect x="6.2" y="3.8" width="5.6" height="10.4" rx="1" fill="#52bdec"/><rect x="7.2" y="5" width="3.6" height="6.4" fill="#fff"/></svg>
          <span>555-386-0942</span>
        </li>
        <li class="contact-item">
          <svg class="contact-icon" viewBox="0 0 18 18"><circle cx="9" cy="9" r="9" fill="#fff"/><rect x="4.5" y="7.5" width="9" height="5.5" rx="1" fill="#52bdec"/><rect x="6.2" y="4.5" width="5.6" height="3" fill="#52bdec"/></svg>
          <span>555-907-1168</span>
        </li>
        <li class="contact-item">
          <svg class="contact-icon" viewBox="0 0 18 18"><circle cx="9" cy="9" r="9" fill="#fff"/><rect x="4.3" y="5.8" width="9.4" height="6.6" rx="0.8" fill="#52bdec"/><path d="M4.6 6.2L9 9.6l4.4-3.4" fill="none" stroke="#fff" stroke-width="1"/></svg>
          <span>hello@vantrelreach.com</span>
        </li>
        <li class="contact-item">
          <svg class="contact-icon" viewBox="0 0 18 18"><circle cx="9" cy="9" r="9" fill="#fff"/><circle cx="9" cy="9" r="4.8" fill="none" stroke="#52bdec" stroke-width="1.2"/><ellipse cx="9" cy="9" rx="2" ry="4.8" fill="none" stroke="#52bdec" stroke-width="1"/><line x1="4.2" y1="9" x2="13.8" y2="9" stroke="#52bdec" stroke-width="1"/></svg>
          <span>www.vantrelreach.com</span>
        </li>
      </ul>
    </div>

    <div class="stripe stripe--right"></div>
    <div class="end-strip"></div>
  </div>
</div>
</body>
</html>
```